Book Cover for Senior Care Agencies

Design a cover [kindle and print] for a book of interviews with home health care agencies, that also has client stories [like a Lantern Pages for the Weary type book]

The title is
Hands That Stay

subtitle
Picking A Fitting Elder Support Service

The book will have 7 co-authors, so they will need to be listed on the cover
Print book Size 6 x 9

For image, I like the idea of an adult helping their senior parent out... What i am going for is very, clean and crisp yet warm. No cartoons.

I don't tend to like script fonts.
thank you

Target Market(s)

Family members who have senior relatives or parents

Industry/Entity Type

Health Care

Font styles to use
Serif
Sans Serif

Requirements
Should not have
• cartoons

```html
<!DOCTYPE html>
<html lang="en">
<head>
<meta charset="utf-8">
<title>Hands That Stay — Book Cover</title>
<link rel="stylesheet" href="https://fonts.googleapis.com/css2?family=Josefin+Sans:wght@400;600;700&family=Questrial&display=swap">
<style>
  :root {
    --backdrop: #2b2b2d;
    --photo-light: #7c879a;
    --photo-mid: #5f6b80;
    --photo-dark: #1f2a42;
    --accent-blue: #12a9ec;
    --title-white: #ffffff;
  }
  html, body {
    margin: 0;
    width: 1200px;
    height: 1200px;
    overflow: hidden;
    background: var(--backdrop);
  }
  .book-cover {
    position: absolute;
    left: 230px;
    top: 45px;
    width: 740px;
    height: 1110px;
    box-shadow: 0 10px 40px rgba(0,0,0,0.55);
    overflow: hidden;
  }
  .cover-photo {
    position: absolute;
    inset: 0;
    background:
      radial-gradient(ellipse at 65% 45%, var(--photo-light) 0%, rgba(124,135,154,0) 60%),
      linear-gradient(160deg, var(--photo-mid) 0%, var(--photo-mid) 55%, var(--photo-dark) 100%);
  }
  .cover-type {
    position: absolute;
    inset: 0;
    width: 740px;
    height: 1110px;
  }
  .subtitle {
    font-family: "Questrial", sans-serif;
    letter-spacing: 3px;
    text-anchor: end;
  }
  .subtitle-white { fill: var(--title-white); font-size: 46px; }
  .subtitle-blue { fill: var(--accent-blue); font-size: 36px; letter-spacing: 1.5px; }
  .title-big {
    font-family: "Josefin Sans", sans-serif;
    font-weight: 600;
    fill: var(--title-white);
  }
  .title-accent {
    font-family: "Josefin Sans", sans-serif;
    font-weight: 700;
    fill: var(--accent-blue);
  }
  .author-name {
    font-family: "Questrial", sans-serif;
    font-size: 27px;
    letter-spacing: 3px;
    fill: var(--title-white);
    text-anchor: end;
  }
  .author-dot { fill: var(--accent-blue); }
</style>
</head>
<body>
  <div class="book-cover">
    <div class="cover-photo" role="img" aria-label="Photo: a smiling adult daughter walking arm in arm with her elderly mother who uses a cane, toned in blue-grey"></div>

    <svg class="cover-type" viewBox="0 0 740 1110" xmlns="http://www.w3.org/2000/svg">
      <g class="subtitle-block">
        <text class="subtitle subtitle-white" x="693" y="91">PICKING A</text>
        <text class="subtitle subtitle-white" x="693" y="140">FITTING</text>
        <text class="subtitle subtitle-blue" x="693" y="184">ELDER SUPPORT</text>
        <text class="subtitle subtitle-blue" x="693" y="225">SERVICE</text>
      </g>

      <g class="title-block">
        <text class="title-big" x="688" y="545" font-size="225" text-anchor="end">That</text>
        <text class="title-accent" x="46" y="558" font-size="58">Hands</text>
        <text class="title-big" x="55" y="732" font-size="220" textLength="610" lengthAdjust="spacingAndGlyphs">Stay</text>
      </g>

      <g class="author-list">
        <text class="author-name" x="641" y="823">AUTHOR 1</text>
        <circle class="author-dot" cx="669" cy="814" r="9.5"/>
        <text class="author-name" x="641" y="857">AUTHOR 2</text>
        <circle class="author-dot" cx="669" cy="848" r="9.5"/>
        <text class="author-name" x="641" y="892">AUTHOR 3</text>
        <circle class="author-dot" cx="669" cy="883" r="9.5"/>
        <text class="author-name" x="641" y="926">AUTHOR 4</text>
        <circle class="author-dot" cx="669" cy="917" r="9.5"/>
        <text class="author-name" x="641" y="961">AUTHOR 5</text>
        <circle class="author-dot" cx="669" cy="952" r="9.5"/>
        <text class="author-name" x="641" y="995">AUTHOR 6</text>
        <circle class="author-dot" cx="669" cy="986" r="9.5"/>
        <text class="author-name" x="641" y="1029">AUTHOR 7</text>
        <circle class="author-dot" cx="669" cy="1020" r="9.5"/>
      </g>
    </svg>
  </div>
</body>
</html>
```